Birchford Realty Business Card

Business Card:

Somewhere on front of card, please include Broker License Number: 5839162

Website is BirchfordRealty.example

Address is:
7218 Crestover Ave E
Saginaw, MI 48271

I'll let you use creative freedom on the rest; we obviously need Name, Title, Email (@BirchfordRealty.example), Office Phone, Cell Phone.

Don't want any special die-cutting, just a standard size business card.

On the back, include a place for the date and time of an appointment to be written in pen.

Requirements
Must have
• Our logo, attached to email.

```html
<!DOCTYPE html>
<html lang="en">
<head>
<meta charset="utf-8">
<title>Birchford Realty Business Card</title>
<link rel="stylesheet" href="https://fonts.googleapis.com/css2?family=Open+Sans:wght@400;600;700&family=Arimo:wght@400&display=swap">
<style>
  :root {
    --canvas: #2b2c2f;
    --navy: #27276f;
    --navy-dark: #1f1f5e;
    --card-white: #ffffff;
    --rule-grey: #b9b9bd;
    --back-top: #f6f6f7;
    --back-bottom: #cfcfd2;
    --ink-light: #e6e6f0;
    --line-dark: #55565c;
  }
  * { box-sizing: border-box; margin: 0; padding: 0; }
  html, body { width: 1200px; height: 871px; overflow: hidden; }
  body {
    background: var(--canvas);
    font-family: "Open Sans", Arial, sans-serif;
    position: relative;
  }
  .card {
    position: absolute;
    top: 281px;
    width: 540px;
    height: 309px;
    overflow: hidden;
    box-shadow: 0 10px 30px rgba(0,0,0,.45);
  }
  .card--front { left: 40px; background: var(--card-white); }
  .card--back {
    left: 620px;
    background: linear-gradient(160deg, var(--back-top) 0%, var(--back-bottom) 100%);
  }

  /* front */
  .band { position: absolute; inset: 0; }
  .brand {
    position: absolute;
    top: 62px;
    right: 56px;
    display: flex;
    align-items: center;
    gap: 10px;
    color: var(--navy);
    font-weight: 700;
    font-size: 34px;
    letter-spacing: -0.5px;
  }
  .brand__dot {
    width: 14px; height: 14px;
    background: var(--navy);
  }
  .person {
    position: absolute;
    left: 26px;
    top: 168px;
    color: var(--ink-light);
    font-family: "Arimo", Arial, sans-serif;
  }
  .person__name { font-family: "Open Sans", Arial, sans-serif; font-weight: 600; font-size: 17px; color: #fff; }
  .person__title { font-size: 13px; margin-bottom: 10px; }
  .person__address { font-size: 12.5px; line-height: 1.4; font-style: normal; }

  .contacts {
    position: absolute;
    right: 22px;
    bottom: 16px;
    list-style: none;
    color: var(--ink-light);
    font-family: "Arimo", Arial, sans-serif;
    font-size: 13px;
    text-align: right;
  }
  .contacts li {
    display: flex; justify-content: flex-end; align-items: center; gap: 8px;
    line-height: 19px;
  }
  .contacts svg { width: 13px; height: 13px; fill: none; stroke: var(--ink-light); stroke-width: 1.6; }
  .contacts .license { padding-right: 21px; }

  /* back */
  .appointment { position: absolute; inset: 0; color: var(--navy); font-size: 11px; }
  .field-label { position: absolute; font-weight: 600; }
  .rule { position: absolute; height: 1px; background: var(--line-dark); }
  .rule--navy { background: var(--navy); height: 1.5px; }
  .ampm { position: absolute; font-size: 8px; right: 40px; top: 52px; }
</style>
</head>
<body>

<section class="card card--front" aria-label="Card front">
  <svg class="band" viewBox="0 0 540 309" preserveAspectRatio="none" aria-hidden="true">
    <defs>
      <linearGradient id="bandFill" x1="0" y1="0" x2="0" y2="1">
        <stop offset="0" stop-color="var(--navy)"/>
        <stop offset="1" stop-color="var(--navy-dark)"/>
      </linearGradient>
    </defs>
    <polygon points="0,132 540,196 540,203 0,139" fill="var(--rule-grey)"/>
    <polygon points="0,141 540,205 540,309 0,309" fill="url(#bandFill)"/>
  </svg>

  <div class="brand"><span class="brand__dot"></span>Birchford Realty</div>

  <div class="person">
    <p class="person__name">Mark Ellison</p>
    <p class="person__title">President</p>
    <address class="person__address">7218 Crestover Ave E<br>Saginaw, MI 48271</address>
  </div>

  <ul class="contacts">
    <li>555 214 7730
      <svg viewBox="0 0 14 14"><path d="M3 2l2 0 1 3-1.5 1a7 7 0 0 0 3.5 3.5L9 8l3 1v2a1 1 0 0 1-1 1A9 9 0 0 1 2 3a1 1 0 0 1 1-1z"/></svg>
    </li>
    <li>555 382 6041
      <svg viewBox="0 0 14 14"><rect x="4" y="1" width="6" height="12" rx="1"/><line x1="6.5" y1="11" x2="7.5" y2="11"/></svg>
    </li>
    <li>name@BirchfordRealty.example
      <svg viewBox="0 0 14 14"><rect x="1" y="3" width="12" height="8"/><path d="M1 3l6 5 6-5"/></svg>
    </li>
    <li>www.BirchfordRealty.example
      <svg viewBox="0 0 14 14"><circle cx="7" cy="7" r="5.5"/><path d="M1.5 7h11M7 1.5c-3 3.5-3 7.5 0 11M7 1.5c3 3.5 3 7.5 0 11"/></svg>
    </li>
    <li class="license">Broker Lic No: 5839162</li>
  </ul>
</section>

<section class="card card--back" aria-label="Card back">
  <div class="appointment">
    <span class="field-label" style="left:34px; top:112px;">Date :</span>
    <div class="rule rule--navy" style="left:34px; width:230px; top:128px;"></div>
    <div class="rule" style="left:78px; width:186px; top:121px;"></div>

    <span class="field-label" style="left:290px; top:56px;">Time :</span>
    <div class="rule rule--navy" style="left:290px; width:210px; top:72px;"></div>
    <span class="ampm">AM/PM</span>
    <div class="rule" style="left:330px; width:170px; top:65px;"></div>

    <div class="rule" style="left:34px; width:466px; top:164px;"></div>
    <div class="rule" style="left:34px; width:466px; top:200px;"></div>
    <div class="rule" style="left:34px; width:466px; top:236px;"></div>
    <div class="rule" style="left:34px; width:466px; top:272px;"></div>
  </div>
</section>

</body>
</html>
```